Used Car Dealer seeks an Amazing Business Card Design

We are looking for a business card design that incorporates our logo and grabs the attention of anyone we give the business card to.

Looking to use the same colors as the logo. Our Logo choice is the black background with Red and Silver/Grey Lettering.

We also would like to see some embossed designs.

Target Market(s)

Used Car Buyers, Automotive, Auto

Industry/Entity Type

Automotive

Contact Information for Business Card

BVEL7K
Gordon Whitlock
482 Tarrow Lane
Suite 207
Roswell, GA 30075
Office (770) 555-0142
Cell (770) 555-0187
bvel7kga@quellmail.com
www.bvel7kga.com

Colors
ffffff
ee3036

Requirements
Must have
• Must include our logo (Black Background with Red and Silver/Grey Lettering)
Nice to have
• Embossed Design. Can be Single or Double Sided.

```html
<!DOCTYPE html>
<html lang="en">
<head>
<meta charset="utf-8">
<title>BVEL7K Business Card</title>
<link rel="stylesheet" href="https://fonts.googleapis.com/css2?family=Roboto+Condensed:wght@300;400;700&family=Roboto:wght@400&display=swap">
<style>
  :root {
    --page: #e4e4e2;
    --card-center: #6b7386;
    --card-mid: #4c5568;
    --card-edge: #2b3545;
    --ink: #ffffff;
    --accent: #ee3036;
    --silver: rgba(170, 176, 186, 0.45);
  }
  html, body {
    margin: 0;
    width: 1200px;
    height: 835px;
    overflow: hidden;
    background: var(--page);
  }
  .card {
    position: absolute;
    left: 40px;
    top: 86px;
    width: 1120px;
    height: 663px;
    overflow: hidden;
    background: radial-gradient(ellipse 62% 70% at 40% 38%, var(--card-center) 0%, var(--card-mid) 50%, var(--card-edge) 100%);
    color: var(--ink);
    font-family: "Roboto", sans-serif;
  }
  .swoosh-area {
    position: absolute;
    left: 0;
    right: 0;
    bottom: 0;
    height: 70px;
    background: linear-gradient(180deg, rgba(170, 176, 186, 0) 0%, var(--silver) 100%);
  }
  .brand {
    position: absolute;
    left: 690px;
    top: 120px;
    display: flex;
    align-items: center;
    gap: 16px;
  }
  .brand-dot {
    width: 22px;
    height: 22px;
    border-radius: 50%;
    background: var(--accent);
  }
  .brand-name {
    font-family: "Roboto Condensed", sans-serif;
    font-weight: 700;
    font-size: 66px;
    letter-spacing: 2px;
    line-height: 1;
    color: var(--ink);
  }
  .holder-name {
    position: absolute;
    left: 198px;
    top: 222px;
    margin: 0;
    font-family: "Roboto Condensed", sans-serif;
    font-weight: 700;
    font-size: 37px;
    line-height: 1.1;
  }
  .holder-role {
    position: absolute;
    left: 198px;
    top: 268px;
    margin: 0;
    font-family: "Roboto Condensed", sans-serif;
    font-weight: 300;
    font-size: 36px;
    line-height: 1.1;
  }
  .contacts {
    position: absolute;
    left: 250px;
    top: 320px;
    margin: 0;
    padding: 0;
    list-style: none;
  }
  .contacts li {
    display: flex;
    align-items: center;
    height: 48px;
    font-size: 28px;
  }
  .contacts svg {
    width: 28px;
    height: 28px;
    margin-right: 26px;
    fill: var(--accent);
  }
</style>
</head>
<body>
<main class="card">
  <div class="swoosh-area" role="img" aria-label="Silver curved swoosh decoration along the lower edge"></div>

  <div class="brand">
    <span class="brand-dot"></span>
    <span class="brand-name">BVEL7K</span>
  </div>

  <h1 class="holder-name">Your Name</h1>
  <p class="holder-role">Position</p>

  <ul class="contacts">
    <li>
      <svg viewBox="0 0 24 24"><path d="M6.6 10.8a15.1 15.1 0 0 0 6.6 6.6l2.2-2.2c.3-.3.7-.4 1-.2 1.1.4 2.3.6 3.6.6.6 0 1 .4 1 1V20c0 .6-.4 1-1 1A17 17 0 0 1 3 4c0-.6.4-1 1-1h3.5c.6 0 1 .4 1 1 0 1.3.2 2.5.6 3.6.1.3 0 .7-.2 1z"/></svg>
      123-456-7890
    </li>
    <li>
      <svg viewBox="0 0 24 24"><path d="M7 1h10a2 2 0 0 1 2 2v18a2 2 0 0 1-2 2H7a2 2 0 0 1-2-2V3a2 2 0 0 1 2-2zm0 3v14h10V4zm5 15.5a1.2 1.2 0 1 0 0 2.4 1.2 1.2 0 0 0 0-2.4z"/></svg>
      123-456-7888
    </li>
    <li>
      <svg viewBox="0 0 24 24"><path d="M2 5h20v14H2zm2 2v.4l8 5.3 8-5.3V7zm0 2.8V17h16V9.8l-8 5.3z"/></svg>
      name@companyname.com
    </li>
    <li>
      <svg viewBox="0 0 24 24"><path d="M12 2a10 10 0 1 0 0 20 10 10 0 0 0 0-20zm6.9 9h-3a15 15 0 0 0-1.3-6 8 8 0 0 1 4.3 6zM12 4c.9 1.3 1.7 3.9 1.9 7h-3.8c.2-3.1 1-5.7 1.9-7zM9.4 5a15 15 0 0 0-1.3 6h-3a8 8 0 0 1 4.3-6zm-4.3 8h3a15 15 0 0 0 1.3 6 8 8 0 0 1-4.3-6zM12 20c-.9-1.3-1.7-3.9-1.9-7h3.8c-.2 3.1-1 5.7-1.9 7zm2.6-1a15 15 0 0 0 1.3-6h3a8 8 0 0 1-4.3 6z"/></svg>
      www.companyname.com
    </li>
    <li>
      <svg viewBox="0 0 24 24"><path d="M12 1a8 8 0 0 0-8 8c0 6 8 14 8 14s8-8 8-14a8 8 0 0 0-8-8zm0 11a3 3 0 1 1 0-6 3 3 0 0 1 0 6z"/></svg>
      address
    </li>
  </ul>
</main>
</body>
</html>
```